Unique and original Business Card for Financial Services Business

I have moved premises and need to change the detail on my business card so thought now is a good time for a re-design. Looking for something professional and modern with colours to fit in with out logo. Like the idea of foil or embossing if that works but not a must have but I do want something that stands out and that I could not design myself.

Once business card is designed I will also be looking to get letterhead and flyers done but want the business card concept in place first.

The majority of designs I am receiving are generic and template based. I am looking for something unique and original. We have some great design elements in our logo, think outside the box and show me something that stands out from the crowd.

Target Market(s)

Business Professionals

Industry/Entity Type

Finance

Contact Information for Business Card

Name: Delia Norwood Phone 0473 958 162 Address PO Box 8617 Mossvale NSW 2389 Email info@steadyharbourfinancialservices.com.au website www.steadyharbourfinancialservices.com.au

Font styles to use
Other font styles liked:
• Ralway

Requirements
Should not have
• No black backgrounds please

```html
<!DOCTYPE html>
<html lang="en">
<head>
<meta charset="utf-8">
<title>Steady Harbour Financial Services – Business Card</title>
<link rel="stylesheet" href="https://fonts.googleapis.com/css2?family=Poppins:wght@300;400&family=Raleway:wght@300&display=swap">
<style>
  :root {
    --stage: #6d6d6d;
    --navy-teal: #00465b;
    --deep-harbour: #0d3542;
    --teal: #0b9090;
    --teal-text: #2fb3b8;
    --white: #ffffff;
    --rule: #2f5866;
  }
  * { box-sizing: border-box; margin: 0; padding: 0; }
  html, body {
    width: 1093px; height: 1200px; overflow: hidden;
    background: var(--stage);
  }
  .card {
    position: absolute;
    left: 265px;
    border-radius: 24px;
    overflow: hidden;
    font-family: "Poppins", sans-serif;
    color: var(--white);
  }
  .card--front {
    top: 226px; width: 577px; height: 357px;
    background: var(--navy-teal);
  }
  .card--back {
    top: 621px; width: 583px; height: 360px;
    background: var(--deep-harbour);
  }

  /* Front */
  .artwork {
    position: absolute; left: 0; top: 0;
    width: 220px; height: 100%;
    background: linear-gradient(100deg, var(--teal) 0%, var(--teal) 30%, #e9f5f5 75%, var(--navy-teal) 100%);
  }
  .identity {
    position: absolute; right: 34px; top: 48px;
    text-align: right; line-height: 1.05;
  }
  .identity__name { font-size: 23px; font-weight: 400; letter-spacing: 0.3px; }
  .identity__role { font-size: 16.5px; font-weight: 400; }

  .contact {
    position: absolute; right: 34px; top: 198px;
    list-style: none; text-align: right;
    font-size: 13px; line-height: 21px;
  }
  .contact li { display: flex; justify-content: flex-end; align-items: center; gap: 5px; white-space: nowrap; }
  .contact svg { width: 13px; height: 13px; flex: none; }
  .address {
    position: absolute; right: 34px; top: 272px;
    text-align: right; font-size: 16px; line-height: 21px; font-style: normal;
  }

  /* Back */
  .brand {
    position: absolute; left: 0; right: 0; top: 78px;
    display: flex; flex-direction: column; align-items: center;
  }
  .brand__square { width: 56px; height: 56px; background: var(--teal); margin-bottom: 24px; }
  .brand__name {
    font-family: "Raleway", sans-serif; font-weight: 300; color: var(--white);
    font-size: 36px; letter-spacing: 0.5px; line-height: 1;
  }
  .brand__tagline {
    font-family: "Raleway", sans-serif; font-weight: 300; color: var(--white);
    font-size: 17px; letter-spacing: 10px; margin-top: 8px; line-height: 1;
  }
  .web-line {
    position: absolute; left: 56px; right: 52px; top: 297px;
    display: flex; align-items: center; gap: 12px;
  }
  .web-line__rule { flex: 1; height: 1px; background: var(--rule); }
  .web-line__url {
    color: var(--teal-text); font-size: 13px; letter-spacing: 1.2px; white-space: nowrap;
  }
</style>
</head>
<body>

<section class="card card--front">
  <div class="artwork" role="img" aria-label="White hummingbird silhouette in flight over a teal panel"></div>

  <header class="identity">
    <p class="identity__name">DELIA NORWOOD</p>
    <p class="identity__role">Managing Director</p>
  </header>

  <ul class="contact">
    <li>0473 958 162
      <svg viewBox="0 0 16 16" aria-hidden="true"><path fill="#fff" d="M3.6 1.5l2.1 2.7-1.3 1.5c.8 2 2.2 3.5 4.2 4.3l1.5-1.3 2.7 2.1-1.1 2.2C6.8 13.5 2.2 8.9 1.4 2.6z"/><path d="M10 2.5a4 4 0 0 1 3.5 3.5M10 .8a6 6 0 0 1 5.2 5.2" stroke="#fff" stroke-width="1.2" fill="none"/></svg>
    </li>
    <li>info@steadyharbourfinancialservices.com.au
      <svg viewBox="0 0 16 16" aria-hidden="true"><rect x="1" y="3" width="14" height="10" fill="#fff"/><path d="M1 3l7 5.5L15 3M1 13l5-5M15 13l-5-5" stroke="#00465b" stroke-width="1" fill="none"/></svg>
    </li>
    <li>www.steadyharbourfinancialservices.com.au
      <svg viewBox="0 0 16 16" aria-hidden="true"><g fill="none" stroke="#fff" stroke-width="1.2"><circle cx="8" cy="8" r="6.6"/><ellipse cx="8" cy="8" rx="3" ry="6.6"/><path d="M1.4 8h13.2M2.5 4.5h11M2.5 11.5h11"/></g></svg>
    </li>
  </ul>

  <address class="address">
    PO Box 8617<br>Mossvale NSW 2389
  </address>
</section>

<section class="card card--back">
  <div class="brand">
    <span class="brand__square"></span>
    <p class="brand__name">STEADY HARBOUR</p>
    <p class="brand__tagline">Financial Services</p>
  </div>
  <div class="web-line">
    <span class="web-line__rule"></span>
    <span class="web-line__url">www.steadyharbourfinancialservices.com.au</span>
    <span class="web-line__rule"></span>
  </div>
</section>

</body>
</html>
```